Portal Panel Medic need professional looking business card printed on plastic, Commericial, Industri

We are family owned and operated garage door company in Indianapolis, Indiana. We sale service and install dock equipment, doors, operators. We are looking to expand our commercial/ industrial division. We also service all residential doors and operators. We are looking for a business that stands out of the crowd. We are committed to have the best customer service in the industry.

Target Market(s)

National and local general contractors, National/ Corpate service accounts,

Industry/Entity Type

Business Service

Contact Information for Business Card

To be printed on plastic stock

Font styles to use
Sans Serif

Colors
ffffff
f04a50
ec1f27

Requirements
Must have
• Name, website,email, phone number, position.
Nice to have
• A standout professional design

```html
<!DOCTYPE html>
<html lang="en">
<head>
<meta charset="utf-8">
<title>Portal Panel Medic – Business Card</title>
<link href="https://fonts.googleapis.com/css2?family=Lato:wght@400;700&display=swap" rel="stylesheet">
<style>
  :root {
    --backdrop: #3a3431;
    --card: #141414;
    --card-edge: #1e1e1e;
    --red: #ec1f27;
    --red-soft: #f04a50;
    --white: #ffffff;
    --grey: #9a9a9a;
    --divider: #2e2e2e;
  }
  * { margin: 0; padding: 0; box-sizing: border-box; }
  html, body {
    width: 1200px; height: 900px; overflow: hidden;
    background: var(--backdrop);
    font-family: "Lato", Arial, sans-serif;
  }
  .canvas { position: relative; width: 1200px; height: 900px; }
  .card {
    position: absolute;
    width: 525px; height: 300px;
    background: var(--card);
    border: 1px solid var(--card-edge);
    box-shadow: 0 10px 30px rgba(0,0,0,.45);
  }
  .card--front { left: 45px; top: 350px; }
  .card--back { left: 630px; top: 250px; }

  .brand {
    color: var(--white);
    font-weight: 400;
    line-height: 1.2;
  }

  .card--front .brand {
    position: absolute; left: 30px; top: 132px; width: 210px;
    font-size: 24px; text-align: center;
  }
  .card--front .divider {
    position: absolute; left: 262px; top: 45px;
    width: 1px; height: 210px; background: var(--divider);
  }
  .person { position: absolute; left: 288px; top: 68px; }
  .person__name { color: var(--red-soft); font-size: 17px; letter-spacing: .3px; }
  .person__role { color: var(--white); font-size: 13px; margin-top: 2px; }
  .contacts { list-style: none; margin-top: 26px; }
  .contacts li {
    display: flex; align-items: center; gap: 8px;
    color: var(--white); font-size: 13px; margin-bottom: 5px;
  }
  .contacts svg { width: 10px; height: 10px; fill: var(--red); flex: none; }

  .card--back .brand {
    position: absolute; left: 0; right: 0; top: 108px;
    text-align: center; font-size: 32px;
  }
  .tagline {
    position: absolute; left: 0; right: 0; bottom: 58px;
    text-align: center; color: var(--grey);
    font-size: 13px; letter-spacing: .8px; text-transform: uppercase;
  }
</style>
</head>
<body>
<div class="canvas">

  <section class="card card--front">
    <p class="brand">Portal Panel Medic</p>
    <div class="divider"></div>
    <div class="person">
      <p class="person__name">MARCUS HALE</p>
      <p class="person__role">Managing Director</p>
      <ul class="contacts">
        <li><svg viewBox="0 0 10 10"><path d="M2 0.5 3.8 2.6 2.9 3.6C3.5 5 5 6.5 6.4 7.1L7.4 6.2 9.5 8 8.3 9.5C4.5 9.2.8 5.5.5 1.7Z"/></svg>317 555 0142</li>
        <li><svg viewBox="0 0 10 10"><path d="M0 2h10v6H0Z M0 2 5 5.5 10 2" stroke="#141414" stroke-width=".8"/></svg>info@portalpanelmedic.com</li>
        <li><svg viewBox="0 0 10 10"><circle cx="5" cy="5" r="5"/><path d="M1 5h8M5 1v8" stroke="#141414" stroke-width=".8"/></svg>www.portalpanelmedic.com</li>
      </ul>
    </div>
  </section>

  <section class="card card--back">
    <p class="brand">Portal Panel Medic</p>
    <p class="tagline">Expert service at an affordable price</p>
  </section>

</div>
</body>
</html>
```